Property Management business needs Business cards designed

We provide a premium property management service based in Sydney's Norther Beaches. We want people to feel confident in choosing us to manage their investment properties. We offer a much more personalized service than other estate agents.
We want a modern clean design. Something that shows confidence without being complicated.
Logo attached.

Target Market(s)

35-70yo Male and Female with strong property portfolios within Sydney's Norther Beaches

Industry/Entity Type

Property Management

Contact Information for Business Card

Address: Suite 7, 12-14 Kelvin Parade, Harlow NSW 2188
Two separate named cards.
Tom Ardley - 0491 570 118 tom@harbourvaleestates.com.au
Clara Dunmore - 0491 570 263 clara@harbourvaleestates.com.au

Requirements
Must have
• Business logo, name, number, address, email.

```html
<!DOCTYPE html>
<html lang="en">
<head>
<meta charset="utf-8">
<title>Harbourvale Estates – Business Card</title>
<link rel="stylesheet" href="https://fonts.googleapis.com/css2?family=Open+Sans:wght@400;600;700&display=swap">
<style>
  :root {
    --page-bg: #d6d6d6;
    --card-bg: #e6e2e1;
    --ink: #1c1c1c;
    --teal: #1f8fa0;
    --teal-light: #3fb1b8;
    --teal-dark: #1a7585;
    --photo-a: #efebea;
    --photo-b: #c9c3c2;
  }
  * { box-sizing: border-box; margin: 0; padding: 0; }
  html, body {
    width: 1200px; height: 1200px; overflow: hidden;
    background: var(--page-bg);
    font-family: "Open Sans", Arial, sans-serif;
    color: var(--ink);
  }
  .card {
    position: absolute; left: 304px; width: 594px; height: 339px;
    background: var(--card-bg); overflow: hidden;
  }
  .card--front { top: 226px; }
  .card--back { top: 629px; }

  .brand {
    position: absolute; display: flex; align-items: center; gap: 10px;
    font-weight: 700; color: var(--ink); letter-spacing: -0.3px; white-space: nowrap;
  }
  .brand__mark { width: 14px; height: 14px; background: var(--teal); flex: none; }
  .card--front .brand { left: 40px; top: 76px; font-size: 27px; }

  .person-name {
    position: absolute; left: 40px; top: 194px;
    font-size: 23px; font-weight: 700; color: var(--teal); letter-spacing: 0.2px;
  }
  .contact-list {
    position: absolute; left: 42px; top: 238px; list-style: none;
    font-size: 12.5px; line-height: 18px;
  }
  .contact-list li { display: flex; align-items: center; gap: 7px; }
  .contact-list svg { width: 11px; height: 11px; flex: none; }
  .contact-list strong { font-weight: 700; }
  .contact-list .email span { font-weight: 400; }

  .office {
    position: absolute; left: 327px; top: 238px;
    font-size: 12.5px; line-height: 18px;
  }
  .office__name { color: var(--teal); }

  .accent-band { position: absolute; left: 0; bottom: 0; width: 594px; height: 16px; }

  .back-visual {
    position: absolute; inset: 0;
    background: radial-gradient(circle at 58% 52%, var(--photo-a) 0 30%, var(--photo-b) 75%);
  }
  .card--back .brand { left: 128px; top: 138px; font-size: 35px; }
  .back-web {
    position: absolute; left: 130px; top: 189px;
    font-size: 13px; font-weight: 700; color: var(--ink);
  }
</style>
</head>
<body>

<section class="card card--front">
  <div class="brand"><span class="brand__mark"></span>HARBOURVALE ESTATES</div>

  <h1 class="person-name">TOM ARDLEY</h1>

  <ul class="contact-list">
    <li>
      <svg viewBox="0 0 12 12"><rect x="1" y="1" width="10" height="10" rx="1.5" fill="none" stroke="var(--teal)" stroke-width="1.4"/><rect x="3" y="3" width="3" height="6" fill="var(--teal)"/></svg>
      0491 570 118
    </li>
    <li class="email">
      <svg viewBox="0 0 12 12"><rect x="0.5" y="2" width="11" height="8" fill="var(--teal)"/><path d="M0.5 2 L6 7 L11.5 2" fill="none" stroke="#fff" stroke-width="1"/></svg>
      <strong>tom</strong><span>@harbourvaleestates.com.au</span>
    </li>
    <li>
      <svg viewBox="0 0 12 12"><circle cx="6" cy="6" r="5" fill="none" stroke="var(--teal)" stroke-width="1.3"/><path d="M1 6 H11 M6 1 C3 4 3 8 6 11 C9 8 9 4 6 1" fill="none" stroke="var(--teal)" stroke-width="0.9"/></svg>
      www.harbourvaleestates.com.au
    </li>
  </ul>

  <address class="office" style="font-style:normal">
    <div class="office__name">Harbourvale Estates</div>
    <div>Suite 7, 12-14 Kelvin Parade,</div>
    <div>Harlow NSW 2188</div>
  </address>

  <svg class="accent-band" viewBox="0 0 594 16" preserveAspectRatio="none">
    <rect x="0" y="0" width="594" height="16" fill="var(--teal-dark)"/>
    <polygon points="0,0 594,0 594,5 0,12" fill="var(--teal-light)"/>
  </svg>
</section>

<section class="card card--back">
  <div class="back-visual" role="img" aria-label="Soft grey photo of a hand sketching a world map globe surrounded by famous landmarks"></div>
  <div class="brand"><span class="brand__mark"></span>HARBOURVALE ESTATES</div>
  <div class="back-web">www.harbourvaleestates.com.au</div>
</section>

</body>
</html>
```